Korrin Baptiste Law website for a law firm

modern clean website for a small boutique law firm. Based in Sacramento, CA and the Bay Area. Practice areas of Family Law, Civil litigation, and Criminal Defense. We already have a logo design as well as attorney pictures to include on page.
Would like images of California included on site.
Would like site to go with Logo that is already designed...blue/grey/white colors.

Industry/Entity Type

Law Firm

Number of Pages Required

5+ page

Requirements
Must have
• I already have several pages of content drafted. Just need the pages with images to input content. Must be clean and modern feel. Want it to reflect California and small boutique feel that is provided personalized legal attention.
• Must have a page where I can blog or post articles on.

```html
<!DOCTYPE html>
<html lang="en">
<head>
<meta charset="utf-8">
<title>Korrin Baptiste Law</title>
<link href="https://fonts.googleapis.com/css2?family=PT+Sans:wght@400;700&family=Raleway:wght@500;600;700&family=Roboto:wght@400;500&family=Poppins:wght@300;400;500&display=swap" rel="stylesheet">
<style>
:root{
  --blue:#3f80c6;
  --blue-deep:#1c6db3;
  --blue-btn:#1f6aa8;
  --ink:#2b2b2b;
  --muted:#6e6e6e;
  --line:#dcdcdc;
  --soft:#f4f4f4;
  --white:#ffffff;
  --night:#0c0c0c;
}
*{margin:0;padding:0;box-sizing:border-box}
html,body{width:1200px;height:2903px;overflow:hidden}
body{position:relative;background:var(--white);font-family:"Poppins",sans-serif;color:var(--ink)}
.abs{position:absolute}

/* top bar */
.topbar{left:0;top:0;width:1200px;height:33px;background:var(--blue);color:var(--white);font:500 12px "Roboto",sans-serif}
.topbar .contact{left:97px;top:9px;display:flex;gap:44px}
.topbar .contact span{display:flex;align-items:center;gap:8px}
.topbar .social{right:104px;top:9px;display:flex;gap:14px}
.dot{width:14px;height:14px;border-radius:50%;background:var(--white);opacity:.9}

/* nav */
.nav{left:0;top:33px;width:1200px;height:52px;background:var(--white)}
.brand{font:500 28px "Raleway",sans-serif;letter-spacing:1px;color:var(--blue)}
.nav .brand{left:97px;top:9px}
.nav ul{list-style:none;right:104px;top:18px;display:flex;gap:40px;font:400 13px "Roboto",sans-serif;color:#333}

/* hero */
.hero{left:0;top:85px;width:1200px;height:459px;background:linear-gradient(180deg,#6f7f8c 0%,#4e5762 35%,#2c3038 70%,#1c1e22 100%)}
.hero h1{left:0;width:1200px;top:165px;text-align:center;font:700 39px "PT Sans",sans-serif;color:var(--white)}
.hero p{left:0;width:1200px;top:231px;text-align:center;font:700 28px/1.55 "PT Sans",sans-serif;color:var(--white)}

/* welcome */
.welcome-title{left:0;width:1200px;top:600px;text-align:center;font:500 33px "Raleway",sans-serif;color:#2a2a2a}
.welcome-text{left:150px;width:900px;top:672px;text-align:center;font:400 11px/25px "Poppins",sans-serif;color:var(--muted)}
.feature{top:762px;height:161px;background:var(--white);border:1px solid var(--line)}
.feature .icon{left:-37px;top:49px;width:72px;height:66px;background:var(--blue);display:flex;align-items:center;justify-content:center}
.feature h3{left:54px;top:28px;font:500 19px "Raleway",sans-serif;color:#2a2a2a;white-space:nowrap}
.feature p{left:54px;top:68px;width:200px;font:400 11px/22px "Poppins",sans-serif;color:var(--muted)}
.feature a{left:54px;top:122px;font:400 11px "Poppins",sans-serif;color:#333;text-decoration:underline}

/* evaluation */
.evaluation{left:0;top:981px;width:1200px;height:404px;background:linear-gradient(90deg,#6d5a46 0%,#9a8a76 40%,#c9c4ba 62%,#ddd8cf 100%)}
.portrait{left:660px;top:0;width:400px;height:404px;background:linear-gradient(180deg,#c9b8a6 0%,#8c8a94 45%,#2d3b55 70%,#1f2a40 100%)}
.form-panel{left:99px;top:25px;width:511px;height:356px;background:rgba(70,60,52,.82)}
.form-panel h2{left:45px;top:38px;display:flex;align-items:center;gap:12px;font:600 19px "Raleway",sans-serif;color:var(--white);letter-spacing:.5px}
.field{height:35px;background:rgba(235,235,235,.82);font:400 12px "Poppins",sans-serif;color:#888;padding:9px 20px}
.field.first{left:42px;top:91px;width:203px}
.field.last{left:259px;top:91px;width:201px}
.field.email{left:42px;top:143px;width:203px}
.field.phone{left:259px;top:143px;width:201px}
.field.message{left:42px;top:196px;width:418px;height:81px}
.submit{left:40px;top:294px;width:166px;height:35px;background:var(--blue);color:var(--white);font:600 14px "Raleway",sans-serif;letter-spacing:.5px;display:flex;align-items:center;justify-content:center}

/* practice areas */
.practice{top:1468px;width:330px}
.practice .icon{left:0;top:0}
.practice h3{left:70px;top:4px;font:500 22px "Raleway",sans-serif;color:#2a2a2a}
.practice .rule{left:70px;top:47px;width:34px;height:2px;background:var(--blue)}
.practice p{left:72px;top:67px;width:250px;font:400 11px/22px "Poppins",sans-serif;color:var(--muted);text-align:justify}

/* blog */
.blog{left:0;top:1670px;width:1200px;height:749px;background:var(--soft)}
.blog h2{left:0;width:1200px;top:52px;text-align:center;font:700 31px "Raleway",sans-serif;color:var(--blue-deep)}
.blog .lead{left:190px;width:820px;top:116px;text-align:center;font:400 10px/23px "Poppins",sans-serif;color:#888}
.post{top:193px;width:485px}
.post .photo{left:0;top:0;width:485px;height:300px;border-radius:6px}
.post h3{left:-4px;top:320px;width:500px;font:600 15px "Raleway",sans-serif;color:#222}
.post p{left:-4px;top:365px;width:490px;font:400 10.5px/22px "Poppins",sans-serif;color:var(--muted)}
.post .more{left:-4px;top:463px;width:118px;height:37px;border-radius:4px;background:var(--blue-btn);color:var(--white);font:600 12px "Raleway",sans-serif;display:flex;align-items:center;justify-content:center;letter-spacing:.5px}

/* call to action */
.cta{left:0;top:2419px;width:1200px;height:143px;background:var(--blue)}
.cta p{left:97px;top:40px;font:400 20px/38px "Roboto",sans-serif;color:var(--white);letter-spacing:.5px}
.cta .btn{left:791px;top:48px;width:310px;height:46px;border:1px solid var(--white);color:var(--white);font:400 20px "Roboto",sans-serif;display:flex;align-items:center;justify-content:center;gap:14px;letter-spacing:.5px}

/* footer */
.footer{left:0;top:2562px;width:1200px;height:341px;background:var(--night);color:var(--white)}
.footer .touch{left:93px;top:40px;font:500 22px "Roboto",sans-serif}
.footer .social{left:292px;top:43px;display:flex;gap:34px}
.footer .social .sq{width:18px;height:18px;border-radius:50%;background:var(--white)}
.footer .feedback{right:104px;top:43px;font:400 13px "Roboto",sans-serif;display:flex;gap:8px;align-items:center}
.footer .divider{left:93px;top:89px;width:1003px;height:1px;background:#3a3a3a}
.footer .brand{left:94px;top:170px;font-size:60px;font-weight:500;color:var(--white);letter-spacing:2px}
.footer h4{font:500 18px "Roboto",sans-serif;top:122px}
.footer ul{list-style:none;top:163px;font:400 12px/21px "Roboto",sans-serif;color:#e8e8e8}
.email-box{left:818px;top:166px;width:277px;height:31px;background:#2f2f2f;display:flex}
.email-box span{flex:1;font:400 12px "Roboto",sans-serif;color:#ddd;padding:8px 10px}
.email-box b{width:38px;background:var(--blue);display:flex;align-items:center;justify-content:center}
.footer .note{left:818px;top:213px;font:500 12px "Roboto",sans-serif}
.footer .copy{left:0;width:1200px;top:306px;text-align:center;font:400 11px "Roboto",sans-serif;color:#9a9a9a}
</style>
</head>
<body>

<header class="topbar abs">
  <div class="contact abs">
    <span><svg width="13" height="10" viewBox="0 0 13 10"><rect x=".5" y=".5" width="12" height="9" fill="none" stroke="#fff"/><path d="M.5 .5 6.5 5.5 12.5 .5" fill="none" stroke="#fff"/></svg>info@kbaptistelaw.com</span>
    <span><svg width="11" height="12" viewBox="0 0 11 12"><path d="M2 1 4 1 5 4 3.5 5C4.3 6.8 5.2 7.7 7 8.5L8 7 11 8 11 10C7 12 -1 5 2 1Z" fill="#fff"/></svg>1800 555 0147</span>
  </div>
  <div class="social abs"><i class="dot"></i><i class="dot"></i><i class="dot"></i><i class="dot"></i><i class="dot"></i></div>
</header>

<nav class="nav abs">
  <div class="brand abs">KBLAW</div>
  <ul class="abs"><li>Home</li><li>About Us</li><li>Services</li><li>Testmonials</li><li>Team</li><li>Contact Us</li></ul>
</nav>

<section class="hero abs" role="img" aria-label="California city skyline at dusk">
  <h1 class="abs">A High-Powered Litigation Boutique</h1>
  <p class="abs">That Beats Larger Firms By Finding The Uniquely<br>Creative, Winning Strategy</p>
</section>

<h2 class="welcome-title abs">Welcome TO KB Law</h2>
<p class="welcome-text abs">Lorem Ipsum is simply dummy text of the printing and typesetting industry. Lorem Ipsum has been the industry's standard dummy text ever since the 1500s,<br>Lorem Ipsum is simply dummy text of the printing and typesetting industry. Lorem Ipsum has been the industry's</p>

<article class="feature abs" style="left:149px;width:267px">
  <div class="icon abs"><svg width="36" height="32" viewBox="0 0 36 32" fill="#fff"><path d="M18 0 36 8V11H0V8Z"/><rect x="4" y="13" width="4" height="12"/><rect x="12" y="13" width="4" height="12"/><rect x="20" y="13" width="4" height="12"/><rect x="28" y="13" width="4" height="12"/><rect x="0" y="27" width="36" height="5"/></svg></div>
  <h3 class="abs">Get Legal Advice</h3>
  <p class="abs">Neque porro quisquam est qui dolo rem ipsum quia dolor sit amet</p>
  <a class="abs">Read More</a>
</article>
<article class="feature abs" style="left:501px;width:269px">
  <div class="icon abs"><svg width="36" height="32" viewBox="0 0 36 32" fill="none" stroke="#fff" stroke-width="2.5"><path d="M18 2V30M8 30H28M4 6H32"/><path d="M4 6 0 17H8Z M32 6 28 17H36Z" fill="#fff"/></svg></div>
  <h3 class="abs">Expert Lawyers</h3>
  <p class="abs">Neque porro quisquam est qui dolo rem ipsum quia dolor sit amet</p>
  <a class="abs">Read More</a>
</article>
<article class="feature abs" style="left:840px;width:273px">
  <div class="icon abs"><svg width="28" height="32" viewBox="0 0 28 32" fill="#fff"><circle cx="14" cy="8" r="7"/><path d="M0 32C0 22 5 17 14 17S28 22 28 32Z"/></svg></div>
  <h3 class="abs">Customer Satisfaction</h3>
  <p class="abs">Neque porro quisquam est qui dolo rem ipsum quia dolor sit amet</p>
  <a class="abs">Read More</a>
</article>

<section class="evaluation abs" role="img" aria-label="Attorney portrait in an office setting">
  <div class="portrait abs"></div>
  <form class="form-panel abs">
    <h2 class="abs"><svg width="22" height="20" viewBox="0 0 22 20" fill="none" stroke="#fff" stroke-width="2"><path d="M13 3H2V18H16V9"/><path d="M9 12 19 2 21 4 11 14 8 15Z"/></svg>FREE CASE EVALUATION</h2>
    <div class="field first abs">First Name</div>
    <div class="field last abs">Last Name</div>
    <div class="field email abs">E-mail</div>
    <div class="field phone abs">Phone</div>
    <div class="field message abs">Messages</div>
    <div class="submit abs">SUBMIT NOW</div>
  </form>
</section>

<div class="practice abs" style="left:87px">
  <svg class="icon abs" width="52" height="52" viewBox="0 0 52 52" fill="var(--blue)"><circle cx="17" cy="12" r="8"/><circle cx="36" cy="15" r="7"/><circle cx="24" cy="30" r="6"/><path d="M2 36C2 26 8 22 17 22S28 25 30 28C22 30 16 34 15 40H2Z"/><path d="M40 24C48 24 52 28 52 38H36C36 32 34 28 31 26 33 25 36 24 40 24Z"/><path d="M12 52C12 42 17 38 24 38S36 42 36 52Z"/></svg>
  <h3 class="abs">Family Law</h3><i class="rule abs"></i>
  <p class="abs">Neque porro quisquam est qui dolorem ipsum quia dolor sit amet Neque porro quisquam est qui dolorem</p>
</div>
<div class="practice abs" style="left:459px">
  <svg class="icon abs" width="50" height="46" viewBox="0 0 50 46" fill="var(--blue)"><rect x="14" y="4" width="10" height="22" transform="rotate(-45 19 15)"/><rect x="20" y="12" width="22" height="6" transform="rotate(45 31 15)"/><rect x="4" y="36" width="36" height="8" rx="2"/></svg>
  <h3 class="abs">Civil litigation</h3><i class="rule abs"></i>
  <p class="abs">Neque porro quisquam est qui dolorem ipsum quia dolor sit amet Neque porro quisquam est qui dolorem</p>
</div>
<div class="practice abs" style="left:815px">
  <svg class="icon abs" width="52" height="44" viewBox="0 0 52 44" fill="none" stroke="var(--blue)" stroke-width="3.5"><circle cx="12" cy="28" r="9"/><circle cx="40" cy="20" r="9"/><path d="M20 24 32 20"/></svg>
  <h3 class="abs">Criminal Defense</h3><i class="rule abs"></i>
  <p class="abs">Neque porro quisquam est qui dolorem ipsum quia dolor sit amet Neque porro quisquam est qui dolorem</p>
</div>

<section class="blog abs">
  <h2 class="abs">Check Out Our Blog</h2>
  <p class="lead abs">Lorem Ipsum is simply dummy text of the printing and typesetting industry. Lorem Ipsum has been the industry's standard dummy text ever since the 1500s, when<br>an unknown printer took a galley of type and scrambled it to make a type specimen book.Lorem Ipsum is simply dummy text</p>
  <article class="post abs" style="left:101px">
    <div class="photo abs" role="img" aria-label="Attorney smiling in front of a bookshelf" style="background:linear-gradient(90deg,#5a3a2a 0%,#7a5a44 40%,#3a3c44 60%,#8a6a52 100%)"></div>
    <h3 class="abs">Lorem Ipsum is simply dummy text of the printing and typesetting</h3>
    <p class="abs">Lorem Ipsum is simply dummy text of the printing and typesetting industry. Lorem Ipsum has been the industry's standard dummy text ever since the 1500s, when an unknown printer took a galley of type and scrambled it to make a type specimen book.</p>
    <div class="more abs">READ MORE</div>
  </article>
  <article class="post abs" style="left:635px">
    <div class="photo abs" role="img" aria-label="Lawyer signing papers beside a gavel and books" style="background:linear-gradient(135deg,#3d5a78 0%,#c9c6c2 45%,#9a7454 75%,#6a4a32 100%)"></div>
    <h3 class="abs">Lorem Ipsum is simply dummy text of the printing and typesetting</h3>
    <p class="abs">Lorem Ipsum is simply dummy text of the printing and typesetting industry. Lorem Ipsum has been the industry's standard dummy text ever since the 1500s, when an unknown printer took a galley of type and scrambled it to make a type specimen book.</p>
    <div class="more abs">READ MORE</div>
  </article>
</section>

<section class="cta abs">
  <p class="abs">If you have any legal problem in your life...<br>We Are Available</p>
  <div class="btn abs">Free Consultation <svg width="16" height="14" viewBox="0 0 16 14" fill="#fff"><path d="M0 5H10V1L16 7 10 13V9H0Z"/></svg></div>
</section>

<footer class="footer abs">
  <div class="touch abs">Get In Touch</div>
  <div class="social abs"><i class="sq"></i><i class="sq"></i><i class="sq"></i><i class="sq"></i></div>
  <div class="feedback abs"><svg width="12" height="8" viewBox="0 0 12 8" fill="none" stroke="#fff" stroke-width="2"><path d="M1 1 6 6 11 1"/></svg>Send Us Feedback</div>
  <i class="divider abs"></i>
  <div class="brand abs">KBLAW</div>
  <h4 class="abs" style="left:401px">Company</h4>
  <ul class="abs" style="left:401px"><li>Team</li><li>Careers</li><li>Terms &amp; Conditions</li><li>Privacy Policy</li><li>Gallery</li></ul>
  <h4 class="abs" style="left:621px">Site Map</h4>
  <ul class="abs" style="left:621px"><li>Home</li><li>About Us</li><li>Services</li><li>Testimonials</li><li>Contact Us</li></ul>
  <h4 class="abs" style="left:818px">Newsletter</h4>
  <div class="email-box abs"><span>enter your email</span><b><svg width="16" height="14" viewBox="0 0 16 14" fill="#fff"><path d="M0 5H10V1L16 7 10 13V9H0Z"/></svg></b></div>
  <div class="note abs">subscribe our latest news, what we do now</div>
  <div class="copy abs">Copyrights © Korrin Baptiste law firm .All Rights Reserved</div>
</footer>

</body>
</html>
```